Clearway Lending Template Design

We need a corporate letterhead template (word) and slide show template (PowerPoint) designed for our Motor Vehicle finance business.

Clearway Lending provides motor vehicle finance to the credit impaired. Please feel free to visit our website www.clearwaylending-example.com

Both templates (word and PowerPoint) must include the Clearway logo (attached to this project) and can be very similar in design.

We are after something creative yet professional in design.

Please feel free to ask any questions.

Thank you
Marisol

```html
<!DOCTYPE html>
<html lang="en">
<head>
<meta charset="utf-8">
<title>Clearway Lending Letterhead</title>
<link rel="stylesheet" href="https://fonts.googleapis.com/css2?family=Questrial&display=swap">
<style>
  :root {
    --paper: #ffffff;
    --band-grey: #6f6f6f;
    --band-green: #2aa534;
    --brand-green: #1f8f2b;
    --mark-grey: #7a7a7a;
    --footer-text: #ffffff;
  }
  html, body {
    margin: 0;
    padding: 0;
    overflow: hidden;
    background: var(--paper);
  }
  .letterhead {
    position: relative;
    width: 849px;
    height: 1200px;
    background: var(--paper);
    overflow: hidden;
    font-family: "Questrial", sans-serif;
  }
  .letterhead__bands {
    position: absolute;
    inset: 0;
  }
  .band-top { fill: var(--band-grey); }
  .band-bottom { fill: var(--band-green); }
  .brand {
    position: absolute;
    top: 43px;
    left: 207px;
    display: flex;
    align-items: center;
    gap: 26px;
  }
  .brand__square {
    width: 108px;
    height: 108px;
    background: var(--mark-grey);
  }
  .brand__name {
    font-size: 40px;
    color: var(--brand-green);
    letter-spacing: 0.5px;
    white-space: nowrap;
  }
  .contact-footer {
    position: absolute;
    left: 0;
    right: 0;
    top: 1152px;
    padding-left: 22px;
    text-align: center;
    color: var(--footer-text);
    font-size: 15.5px;
    line-height: 21px;
  }
  .contact-footer p { margin: 0; }
  .contact-footer .gap { display: inline-block; width: 18px; }
</style>
</head>
<body>
  <main class="letterhead">
    <svg class="letterhead__bands" width="849" height="1200" viewBox="0 0 849 1200" aria-hidden="true">
      <polygon class="band-top" points="0,0 822,0 780,29 98,29 0,98"/>
      <polygon class="band-bottom" points="30,1200 92,1140 755,1140 849,1073 849,1200"/>
    </svg>

    <header class="brand">
      <div class="brand__square"></div>
      <div class="brand__name">Clearway Lending</div>
    </header>

    <footer class="contact-footer">
      <p>Clearway Lending Pty Ltd<span class="gap"></span>|&nbsp; PO Box 418 Ashvale VIC 3190</p>
      <p>t. 1300 555 014<span class="gap"></span>e. info@clearwaylending-example.com</p>
    </footer>
  </main>
</body>
</html>
```